24/7 Gym Membership Pricing Card (A6)

I need a pricing card with the different membership options on it.

The membership options are;

12 Month Minimum Term:
No Joining Fee, $25 Access Card Fee, $12.25 per week

No Contract:
$89 Joining Fee, $55 Access Card Fee, $13.50 per week

Pay in Advance:
12 Month - $540
6 Month - $295
3 Month - $190

I have attached our old pricing card below for reference.

Our Logo is also attached.

Target Market(s)

Potential members

Industry/Entity Type

Fitness

Colors
f37122
f68e4e
f9bb94
f78f20
faa54b
fbc994

Requirements
Must have
• My Logo, pricing options
Nice to have
• Contact details; 4819 2653, halloway@vantrofit.com.au, www.vantrofit.com.au
• Our staffed hours; Mon-Thur: 12pm - 7pm, Fri-Sat: 8am - 1pm
Should not have
• Wasted space

```html
<!DOCTYPE html>
<html lang="en">
<head>
<meta charset="utf-8">
<title>Membership Options – Vantro Fit Halloway</title>
<link href="https://fonts.googleapis.com/css2?family=Montserrat:wght@400;500;700;800&display=swap" rel="stylesheet">
<style>
  :root {
    --orange: #f37122;
    --orange-mid: #f78f20;
    --orange-soft: #faa54b;
    --orange-pale: #fbc994;
    --ink: #1a1a1a;
    --charcoal: #2b2b2b;
    --cell: rgba(40, 40, 42, 0.88);
    --header-cell: rgba(60, 60, 62, 0.85);
    --column-wash: rgba(120, 120, 125, 0.35);
    --white: #ffffff;
  }
  * { margin: 0; padding: 0; box-sizing: border-box; }
  html, body { width: 1200px; height: 848px; overflow: hidden; background: #ddd; }
  body { font-family: "Montserrat", sans-serif; color: var(--white); }

  .card { position: relative; width: 1200px; height: 848px; overflow: hidden; }

  .hero-photo {
    position: absolute; left: 0; top: 0; width: 1200px; height: 725px;
    background:
      radial-gradient(ellipse at 80% 40%, rgba(220, 190, 170, 0.55), transparent 55%),
      radial-gradient(ellipse at 15% 10%, rgba(243, 113, 34, 0.55), transparent 50%),
      linear-gradient(160deg, #9a8a80 0%, #6f6a6a 40%, #4c4c52 75%, #3a3a40 100%);
  }

  .title-band {
    position: absolute; left: 0; top: 34px; width: 1200px; height: 66px;
    background: linear-gradient(90deg, rgba(251, 201, 148, 0.9) 0%, rgba(249, 187, 148, 0.75) 45%, rgba(243, 113, 34, 0.15) 100%);
  }
  .title {
    position: absolute; left: 26px; top: 45px;
    font-weight: 800; font-size: 38px; letter-spacing: 0.5px; color: var(--ink);
  }

  .column-wash { position: absolute; top: 208px; width: 232px; height: 368px; background: var(--column-wash); }
  .column-head {
    position: absolute; top: 136px; width: 232px; height: 60px;
    background: var(--header-cell);
    display: flex; align-items: center; justify-content: center; text-align: center;
    font-weight: 700; font-size: 18px; line-height: 1.15; text-transform: uppercase;
  }
  .col-1 { left: 29px; } .col-2 { left: 276px; } .col-3 { left: 524px; }

  .price-row { position: absolute; left: 12px; width: 759px; height: 75px; background: var(--cell); box-shadow: 0 3px 8px rgba(0,0,0,0.35); }
  .row-1 { top: 252px; } .row-2 { top: 347px; } .row-3 { top: 436px; }
  .price {
    position: absolute; top: 0; height: 75px; width: 240px;
    display: flex; flex-direction: column; align-items: center; justify-content: center; text-align: center;
  }
  .price .amount { font-weight: 800; font-size: 38px; line-height: 1; }
  .price .label { font-weight: 500; font-size: 18px; line-height: 1.1; margin-top: 2px; }
  .price.p-1 { left: 15px; } .price.p-2 { left: 262px; } .price.p-3 { left: 512px; }
  .price.p-3 .label { order: -1; font-weight: 700; font-size: 19px; margin: 0 0 2px; }

  .hours-band {
    position: absolute; left: 0; top: 606px; width: 1200px; height: 119px;
    background: rgba(40, 40, 44, 0.8);
  }
  .hours-title { position: absolute; left: 26px; top: 616px; font-size: 29px; font-weight: 400; }
  .hours-line { position: absolute; left: 26px; top: 654px; font-size: 31px; font-weight: 700; white-space: nowrap; }
  .hours-line .days { color: var(--orange-mid); }

  .footer { position: absolute; left: 0; top: 725px; width: 1200px; height: 123px; background: var(--charcoal); }
  .brand-panel {
    position: absolute; left: 0; top: 725px; width: 404px; height: 123px; background: var(--orange);
    display: flex; align-items: center; justify-content: center; gap: 12px;
  }
  .brand-mark { width: 22px; height: 22px; border-radius: 50%; background: var(--white); }
  .brand-name { font-weight: 800; font-size: 34px; letter-spacing: 1px; color: var(--white); text-transform: uppercase; }

  .contact-list { position: absolute; left: 440px; top: 740px; list-style: none; }
  .contact-list li { display: flex; align-items: center; height: 31px; font-size: 20px; font-weight: 500; }
  .contact-list svg { width: 20px; height: 20px; margin-right: 30px; fill: none; stroke: var(--orange); stroke-width: 2; }

  .team-photo {
    position: absolute; left: 988px; top: 664px; width: 176px; height: 184px;
    background: linear-gradient(180deg, rgba(200, 170, 150, 0.35), rgba(90, 80, 80, 0.6));
  }
</style>
</head>
<body>
<main class="card">
  <div class="hero-photo" role="img" aria-label="Photo of a woman doing sit-ups on a bench in a gym"></div>

  <div class="title-band"></div>
  <h1 class="title">MEMBERSHIP OPTIONS</h1>

  <div class="column-wash col-1"></div>
  <div class="column-wash col-2"></div>
  <div class="column-wash col-3"></div>

  <div class="column-head col-1">12 Month<br>Minimum Term</div>
  <div class="column-head col-2">No<br>Contract</div>
  <div class="column-head col-3">Pay in<br>Advance</div>

  <div class="price-row row-1">
    <div class="price p-1"><span class="amount">$0.00</span><span class="label">Joining Fee</span></div>
    <div class="price p-2"><span class="amount">$89.00</span><span class="label">Joining Fee</span></div>
    <div class="price p-3"><span class="amount">$540.00</span><span class="label">12 Month</span></div>
  </div>
  <div class="price-row row-2">
    <div class="price p-1"><span class="amount">$25.00</span><span class="label">Access Card Fee</span></div>
    <div class="price p-2"><span class="amount">$55.00</span><span class="label">Access Card Fee</span></div>
    <div class="price p-3"><span class="amount">$295.00</span><span class="label">6 Month</span></div>
  </div>
  <div class="price-row row-3">
    <div class="price p-1"><span class="amount">$12.25</span><span class="label">per week</span></div>
    <div class="price p-2"><span class="amount">$13.50</span><span class="label">per week</span></div>
    <div class="price p-3"><span class="amount">$190.00</span><span class="label">3 Month</span></div>
  </div>

  <div class="hours-band"></div>
  <p class="hours-title">Our staffed hours-</p>
  <p class="hours-line"><span class="days">Mon-Thur :</span> 12.00pm - 7.00pm&nbsp;&nbsp;<span class="days">Fri-Sat :</span> 8.00am - 1.00pm</p>

  <div class="team-photo" role="img" aria-label="Photo of a man and a woman holding dumbbells"></div>

  <footer>
    <div class="footer"></div>
    <div class="brand-panel">
      <span class="brand-mark"></span>
      <span class="brand-name">Vantro Fit</span>
    </div>
    <ul class="contact-list">
      <li><svg viewBox="0 0 24 24"><path d="M5 3h4l2 5-3 2a12 12 0 0 0 6 6l2-3 5 2v4a2 2 0 0 1-2 2A18 18 0 0 1 3 5a2 2 0 0 1 2-2z"/></svg>07 4819 2653</li>
      <li><svg viewBox="0 0 24 24"><rect x="3" y="5" width="18" height="14"/><path d="M3 5l9 7 9-7"/></svg>halloway@vantrofit.com.au</li>
      <li><svg viewBox="0 0 24 24"><rect x="3" y="4" width="18" height="12"/><path d="M9 20h6M12 16v4"/></svg>www.vantrofit.com.au</li>
    </ul>
  </footer>
</main>
</body>
</html>
```